www.brightlingua.net -- International Language school needs a Wordpress Design

NOTE: This is for a complete WordPress website with coding (Design/develop)

We are a small, private English language school in business for 15 years. Our students come from around the world to study English at our centre in Toronto, Canada. Most of our students are in their 20's and come to study English with us for periods of 1-6 months before returning home to complete their post-secondary education or pursue their careers.

We are looking for a talented web designer to redevelop our sadly outdated website (www.brightlingua.net) to bring a fresh look with vastly increased functionality and web traffic.

Target Market(s)

-20s and 30s; mostly upper-middle class, educated
-from non-English speaking countries, but often have some English background
-looking to improve their English (mostly speaking) skills at our school like ours and experience living in a new country (like exchange students)

Industry/Entity Type

Education

Font styles to use
Sans Serif

Requirements
Must have
• - page listing our programs
- page with our fees and starting dates
- application form
- page showing why BRIGHT (us)?
- page with accommodation options
* responsive design
Nice to have
• examples of other websites in our industry I like:

http://www.halvorsenlang.com/
http://www.pqlearning.com/en
http://en.rtz.ca/
http://www.marstowe-academy.ac.uk/

```html
<!DOCTYPE html>
<html lang="en">
<head>
<meta charset="utf-8">
<title>BRIGHT – Private English Language Learning School</title>
<link rel="stylesheet" href="https://fonts.googleapis.com/css2?family=Open+Sans:wght@400;600&display=swap">
<style>
:root{
  --blue:#2a87c8;
  --blue-dark:#1f6fa8;
  --green:#8cc21a;
  --green-light:#a3d532;
  --orange:#f7a414;
  --ink:#222;
  --muted:#555;
  --line:#e3e3e3;
  --panel:#f3f3f3;
}
*{box-sizing:border-box;margin:0;padding:0}
html,body{width:918px;height:1200px;overflow:hidden;background:#fff}
body{font-family:"Open Sans",Arial,sans-serif;color:var(--ink);position:relative}
.wrap{position:absolute;left:115px;width:688px}

/* header */
.site-header{height:94px;position:relative}
.brand{position:absolute;left:116px;top:30px;display:flex;align-items:center;gap:8px}
.brand-mark{width:22px;height:22px;border-radius:50%;background:var(--blue)}
.brand-name{font-size:28px;font-weight:600;color:#1a1a1a;letter-spacing:1px}
.lang-select{position:absolute;right:116px;top:13px;width:67px;height:19px;border:1px solid #ccc;border-radius:2px;font-size:8px;display:flex;align-items:center;gap:4px;padding-left:6px;color:#333;background:#fafafa}
.lang-flag{width:12px;height:8px;background:#2b3f8c}
.contact{position:absolute;right:116px;top:42px;text-align:right;font-size:7.5px;line-height:14px;color:#333}
.contact .phone{font-size:8.5px}

/* nav */
.main-nav{position:absolute;top:94px;left:0;width:918px;height:33px;background:linear-gradient(#a3d532,#86bd16)}
.main-nav ul{list-style:none;display:flex;position:absolute;left:140px;top:0;height:33px;align-items:center}
.main-nav li{color:#fff;font-size:11px;margin-right:28px}

/* hero */
.hero{position:absolute;top:127px;left:0;width:918px;height:323px;background:linear-gradient(100deg,#5b5149 0%,#8a7a6b 35%,#b59d86 55%,#6d8ca0 80%,#4d5660 100%)}
.hero-label{position:absolute;left:115px;top:127px;width:267px;height:73px;background:rgba(42,135,200,.92);clip-path:polygon(0 0,100% 0,93% 100%,0 100%);color:#fff;padding:12px 0 0 24px}
.hero-label h1{font-weight:400;font-size:23px;line-height:26px;letter-spacing:.3px}
.hero-label p{font-size:15px;line-height:19px}
.hero-dots{position:absolute;left:436px;top:300px;display:flex;gap:3px}
.hero-dots span{width:10px;height:10px;border-radius:50%;background:#fff}
.hero-dots span:first-child{background:#111}

/* quick links */
.quick-links{position:absolute;top:477px;left:115px;width:688px;display:flex}
.quick-link{flex:1;text-align:center;border-right:1px solid var(--line);height:82px;padding-top:8px}
.quick-link:last-child{border-right:0}
.quick-link svg{display:block;margin:0 auto 6px}
.quick-link h3{font-weight:400;font-size:11.5px;color:var(--blue)}
.quick-link p{font-size:6.5px;color:#444;margin-top:3px}

/* intro */
.intro{top:594px;text-align:center}
.intro h2{font-weight:400;font-size:19px;color:#111}
.intro p{font-size:7.5px;line-height:14px;color:#444;margin-top:8px;padding:0 40px}

/* feature cards */
.features{top:696px;display:flex;gap:8px}
.feature{width:224px;height:158px;position:relative}
.feature .ph{height:110px}
.feature .cap{height:48px;color:#fff;padding:7px 16px}
.feature h3{font-weight:400;font-size:13px}
.feature p{font-size:8.5px;opacity:.9;margin-top:2px}
.cap-blue{background:var(--blue)}
.cap-orange{background:var(--orange)}
.cap-green{background:var(--green)}

/* programs band */
.programs-band{position:absolute;top:895px;left:0;width:918px;height:229px;background:var(--panel);border-top:1px solid var(--line)}
.section-title{position:absolute;font-weight:400;font-size:15.5px;color:#111}
.program{position:absolute;top:946px;width:146px;height:147px;background:#fff;border:1px solid #ddd}
.program .ph{height:76px}
.program h4{font-weight:400;font-size:8.8px;line-height:12px;color:var(--blue);padding:8px 11px 0}
.program p{font-size:6.5px;line-height:11.5px;color:#555;padding:4px 11px 0}
.video{position:absolute;left:596px;top:946px;width:207px;height:140px;background:linear-gradient(120deg,#6e4a2a,#b48158 50%,#d9cbb8)}
.play{position:absolute;left:89px;top:55px;width:28px;height:28px;border-radius:50%;background:#fff}

/* footer */
.site-footer{position:absolute;top:1124px;left:0;width:918px;height:76px;border-top:1px solid var(--line)}
.footer-links{position:absolute;left:117px;top:25px;font-size:8px;color:#333}
.copyright{position:absolute;left:117px;top:44px;font-size:7.5px;color:#333}
.partners{position:absolute;left:500px;top:22px;display:flex;gap:14px;align-items:center}
.badge{height:28px;background:#c9d6e4;border-radius:3px}
</style>
</head>
<body>

<header class="site-header">
  <div class="brand"><span class="brand-mark"></span><span class="brand-name">BRIGHT</span></div>
  <div class="lang-select"><span class="lang-flag"></span>English ▾</div>
  <address class="contact" style="font-style:normal">
    418 Wellmont Avenue, Suite 12, Toronto,<br>
    Ontario, M5R 3K9 Canada<br>
    <span class="phone">Phone number: +1-416-555-0182</span>
  </address>
</header>

<nav class="main-nav">
  <ul>
    <li>Home</li><li>Our School</li><li>Programs</li><li>Fees &amp; Dates</li><li>Accommodation</li><li>After Class</li><li>Agent</li><li>Contact</li>
  </ul>
</nav>

<section class="hero" role="img" aria-label="Photo of two smiling students in a classroom">
  <div class="hero-label">
    <h1>PRIVATE ENGLISH</h1>
    <p>Language Learning school</p>
  </div>
  <div class="hero-dots"><span></span><span></span><span></span><span></span></div>
</section>

<section class="quick-links">
  <div class="quick-link">
    <svg width="28" height="26" viewBox="0 0 28 26" fill="#2a87c8"><circle cx="14" cy="7" r="5"/><circle cx="5" cy="9" r="3.5"/><circle cx="23" cy="9" r="3.5"/><path d="M6 25c0-7 3-11 8-11s8 4 8 11z"/><path d="M0 22c0-5 2-8 5-8 1.5 0 2.5.5 3 1-1.5 2-2.3 4.5-2.5 7z"/><path d="M28 22c0-5-2-8-5-8-1.5 0-2.5.5-3 1 1.5 2 2.3 4.5 2.5 7z"/></svg>
    <h3>Meet Our Students</h3><p>Lorem ipsum dolor sit amet conse</p>
  </div>
  <div class="quick-link">
    <svg width="28" height="26" viewBox="0 0 28 26" fill="none" stroke="#2a87c8" stroke-width="2"><rect x="2" y="5" width="18" height="18" rx="2"/><path d="M10 17l2-5 11-11 3 3-11 11z" fill="#fff"/></svg>
    <h3>Admissions</h3><p>Praesent elementum elit at tellus</p>
  </div>
  <div class="quick-link">
    <svg width="28" height="26" viewBox="0 0 28 26"><circle cx="14" cy="13" r="12" fill="#2a87c8"/><path d="M10 10a4 4 0 1 1 5.5 3.7c-1 .5-1.5 1-1.5 2.3" stroke="#fff" stroke-width="2.4" fill="none"/><circle cx="14" cy="20" r="1.5" fill="#fff"/></svg>
    <h3>Got a Question?</h3><p>Lorem ipsum dolor sit amet consect</p>
  </div>
  <div class="quick-link">
    <svg width="32" height="26" viewBox="0 0 32 26" fill="#2a87c8"><path d="M16 3l16 7-16 7-16-7z"/><path d="M7 14v6c3 3 15 3 18 0v-6l-9 4z"/><rect x="28" y="10" width="1.6" height="9"/></svg>
    <h3>Our Courses</h3><p>Praesent elementum elit at tellus</p>
  </div>
  <div class="quick-link">
    <svg width="28" height="26" viewBox="0 0 28 26"><circle cx="14" cy="13" r="12" fill="#2a87c8"/><path d="M8 13l4 4 8-8" stroke="#fff" stroke-width="3" fill="none"/></svg>
    <h3>Apply Now</h3><p>Lorem ipsum dolor sit amet consect</p>
  </div>
</section>

<section class="wrap intro">
  <h2>Mauris vel lacus vitae felis vestibulum volutpat est nunc</h2>
  <p>cligula augue bibendum accumsan vestibulum ut commodo a mi Morbi ornare gravida elit Integer congue augue et malesuada iaculis ipsum dui aliquet felis at cursus magna nisl nec elit Praesent elementum elit at tellus nec ultricies sit amet porttitor mattis enim In massa libero interdum nec interdum vel blandit sed nulla In ullamcorper est eget tempor cursus neque mi consectetuer mi a ultricies massa est sed nisl Class apte</p>
</section>

<section class="wrap features">
  <article class="feature">
    <div class="ph" role="img" aria-label="Photo of students around a classroom table" style="background:linear-gradient(135deg,#d8cfa8,#9a8a6a)"></div>
    <div class="cap cap-blue"><h3>Fees &amp; Dates</h3><p>Curabitur iaculis tempus eros Curabitur vel</p></div>
  </article>
  <article class="feature">
    <div class="ph" role="img" aria-label="Photo of smiling young students outdoors" style="background:linear-gradient(135deg,#3b3a2e,#8aa85a 60%,#c9a98a)"></div>
    <div class="cap cap-orange"><h3>Recent News</h3><p>Curabitur iaculis tempus eros Curabitur vel</p></div>
  </article>
  <article class="feature">
    <div class="ph" role="img" aria-label="Photo of a student group in life jackets on a boat trip" style="background:linear-gradient(135deg,#4a6a8a,#c0564a 55%,#d8b080)"></div>
    <div class="cap cap-green"><h3>Photo Gallery</h3><p>Curabitur iaculis tempus eros Curabitur vel</p></div>
  </article>
</section>

<section class="programs-band"></section>
<h2 class="section-title" style="left:112px;top:920px">Our Programs</h2>
<h2 class="section-title" style="left:592px;top:919px">Watch Our Video</h2>

<article class="program" style="left:115px">
  <div class="ph" role="img" aria-label="Photo of students studying together" style="background:linear-gradient(135deg,#b8a888,#5a4a3a)"></div>
  <h4>Full-Time Programs<br>Intensive Focus</h4>
  <p>Class aptent taciti sociosqu ad litora torquent per conubia nostra</p>
</article>
<article class="program" style="left:270px">
  <div class="ph" role="img" aria-label="Photo of a parent and children at home" style="background:linear-gradient(135deg,#e0ddd5,#3a5a8a)"></div>
  <h4>Junior Programs<br>Parent &amp; Child</h4>
  <p>Class aptent taciti sociosqu ad litora torquent per conubia nost</p>
</article>
<article class="program" style="left:426px">
  <div class="ph" role="img" aria-label="Photo of a group of smiling young students" style="background:linear-gradient(135deg,#a88a6a,#5a3a2a 60%,#d8c0a8)"></div>
  <h4>Special Programs<br>University Bridge</h4>
  <p>Class aptent taciti sociosqu ad litora torquent per conubia nost.</p>
</article>

<div class="video" role="img" aria-label="Video still of students working at a desk">
  <div class="play"><svg width="28" height="28" viewBox="0 0 28 28"><path d="M11 8l9 6-9 6z" fill="#111"/></svg></div>
</div>

<footer class="site-footer">
  <div class="footer-links">Home &nbsp;|&nbsp; Our School &nbsp;|&nbsp; Programs &nbsp;|&nbsp; Fees &amp; Dates &nbsp;|&nbsp; Accommodation &nbsp;|&nbsp; After Class &nbsp;|&nbsp; Agent</div>
  <div class="copyright">© 2015 Company Name &nbsp;All right reserved &nbsp;Term of Use</div>
  <div class="partners">
    <span class="badge" style="width:52px"></span>
    <span class="badge" style="width:62px"></span>
    <span class="badge" style="width:44px"></span>
    <span class="badge" style="width:24px;border-radius:50%"></span>
    <span class="badge" style="width:58px"></span>
  </div>
</footer>

</body>
</html>
```